Business card for utility of the future

I need a business card template designed for brookvane. We provide sustainable water, energy and waste services to homes.

The card should include name, position, email address, phone number, website and our logo (attached). I would like it to convey professionalism and creativity.

Target Market(s)

Homeowners, investors, corporate partners.

Industry/Entity Type

Utility

Contact Information for Business Card

The card should include name, position, email address, phone number, website and our logo (attached).

```html
<!DOCTYPE html>
<html lang="en">
<head>
<meta charset="utf-8">
<title>brookvane business card</title>
<link href="https://fonts.googleapis.com/css2?family=Poppins:wght@400;500;600&display=swap" rel="stylesheet">
<style>
  :root {
    --bg: #ececec;
    --paper: #ffffff;
    --ink: #111111;
    --muted: #444444;
    --green: #4fa866;
    --orange: #e0703f;
    --peach: #e9a68a;
    --black-card: #0d0d0d;
    --white: #ffffff;
  }
  * { box-sizing: border-box; margin: 0; padding: 0; }
  html, body {
    width: 1200px; height: 770px; overflow: hidden;
    background: var(--bg);
    font-family: "Poppins", sans-serif;
  }
  .sheet {
    position: relative; width: 1200px; height: 770px;
    display: flex; align-items: center; justify-content: center; gap: 30px;
  }
  .card {
    position: relative; width: 525px; height: 300px;
    box-shadow: 0 6px 18px rgba(0,0,0,0.12);
    overflow: hidden;
  }
  .card--front { background: var(--paper); }
  .card--back {
    background: var(--black-card);
    display: flex; align-items: center; justify-content: center;
  }
  .company-name {
    font-weight: 500; line-height: 1; letter-spacing: 0;
  }
  .card--front .company-name {
    position: absolute; left: 40px; top: 40px; font-size: 36px; color: var(--ink);
  }
  .card--back .company-name { font-size: 52px; color: var(--white); }
  .identity { position: absolute; left: 40px; top: 108px; }
  .identity__name {
    font-size: 19px; font-weight: 600; color: var(--ink); letter-spacing: 1.5px;
  }
  .identity__role { font-size: 13px; color: var(--green); margin-top: 2px; }
  .identity__address { font-size: 11.5px; color: var(--muted); line-height: 1.45; margin-top: 8px; }
  .contacts {
    position: absolute; right: 40px; bottom: 36px; list-style: none;
    font-size: 12px; color: var(--ink);
  }
  .contacts__item { display: flex; align-items: center; gap: 9px; line-height: 1.75; }
  .contacts__icon { width: 10px; height: 10px; flex: none; }
  .strip { position: absolute; left: 0; right: 0; bottom: 0; height: 9px; display: flex; }
  .strip__black { flex: 60; background: var(--ink); }
  .strip__green { flex: 30; background: var(--green); }
  .strip__orange { flex: 10; background: var(--orange); }
</style>
</head>
<body>
<main class="sheet">
  <section class="card card--front" aria-label="Card front">
    <p class="company-name">brookvane</p>
    <div class="identity">
      <p class="identity__name">DANIEL REYES</p>
      <p class="identity__role">President &amp; CEO</p>
      <p class="identity__address">245 Larkspur Ave<br>Fairhaven, IN 46010</p>
    </div>
    <ul class="contacts">
      <li class="contacts__item">
        <svg class="contacts__icon" viewBox="0 0 10 10"><rect width="10" height="10" rx="2" fill="var(--orange)"/></svg>
        317-555-0148
      </li>
      <li class="contacts__item">
        <svg class="contacts__icon" viewBox="0 0 10 10"><rect width="10" height="10" rx="2" fill="var(--peach)"/></svg>
        hello@brookvane.com
      </li>
      <li class="contacts__item">
        <svg class="contacts__icon" viewBox="0 0 10 10"><rect width="10" height="10" rx="2" fill="var(--peach)"/></svg>
        www.brookvane.com
      </li>
    </ul>
    <div class="strip"><span class="strip__black"></span><span class="strip__green"></span><span class="strip__orange"></span></div>
  </section>
  <section class="card card--back" aria-label="Card back">
    <p class="company-name">brookvane</p>
  </section>
</main>
</body>
</html>
```